Red Gum Wrecking P/L business card

I already have a EPS logo design that I wish to use however, the company is a demolition company based on the Central Coast of NSW Australia. The company is called "Red Gum Wrecking P/L".

We offer demolition services such as Residential, Commercial, Civil, Asbestos removal, Excavation and Tree removal that are required to be displayed on the rear of the business card.

We currently have 4 personnel that require business cards with their specific contact details.

The logo is mid blue on a white background and the remainder is black text on a whiter card.

The eps logo supplied should only be displayed as a logo without the text.

Target Market(s)

People, governments, companies requiring demolition services on the east coast of NSW, specifically Central Coast, Sydney and Newcastle locations.

Industry/Entity Type

Business

Contact Information for Business Card

There are four cards required
First card:
Martin Elsby
Operations Director
Mobile No. 0462 815094
E: info@redgumwreck.com.au
www.redgumwreck.com.au
Second card:
Peter Halloran
Project Director
Company Mobile: 0462 815094
Personal Mobile: 0428 160 384
www.redgumwreck.com.au
Third card:
Simon Preddy
Project Director
Company Mobile: 0462 815 094
Personal Mobile: 0433 958217
www.redgumwreck.com.au
Fourth card:
Neil Brathwaite
General Manager
Personal Mobile: 0437 281609
www.redgumwreck.com.au

Font styles to use
Other font styles liked:
• Helvetica

Colors
33a6d7

Requirements
Must have
• The RGW logo (without the text of Red Gum Wrecking)
Horizontal layout with logo on top left hand corner
Services provision on the rear of the card
Nice to have
• Logo on top left corner
Text should be something like Helvetica
Should not have
• Do not include the text that is incorporated in the EPS file I sent ….just the logo

```html
<!DOCTYPE html>
<html lang="en">
<head>
<meta charset="utf-8">
<title>Red Gum Wrecking P/L – Business Cards</title>
<link rel="stylesheet" href="https://fonts.googleapis.com/css2?family=Mulish:wght@400;700&display=swap">
<style>
  :root {
    --bg: #e6e9eb;
    --card: #ffffff;
    --card-tint: #f4f6f7;
    --brand: #1f9fc0;
    --brand-soft: #5db4cb;
    --muted: #3a9cb8;
    --shadow: rgba(0, 0, 0, 0.18);
  }
  * { box-sizing: border-box; margin: 0; padding: 0; }
  html, body {
    width: 1200px; height: 1000px; overflow: hidden;
    background: var(--bg);
    font-family: "Mulish", "Helvetica", Arial, sans-serif;
    color: var(--brand);
  }
  .sheet {
    width: 1200px; height: 1000px;
    display: grid;
    grid-template-columns: 540px 540px;
    grid-template-rows: repeat(3, 300px);
    gap: 25px 40px;
    padding: 25px 40px;
  }
  .card {
    position: relative;
    background: linear-gradient(135deg, var(--card) 0%, var(--card-tint) 100%);
    box-shadow: 0 4px 14px var(--shadow);
  }
  .brand-mark {
    position: absolute; left: 56px; top: 78px;
    display: flex; align-items: center; gap: 10px;
    font-weight: 400; font-size: 64px; letter-spacing: 2px;
    color: var(--brand-soft); line-height: 1;
  }
  .brand-mark .dot {
    width: 12px; height: 12px; background: var(--brand-soft);
  }
  .person { position: absolute; left: 290px; top: 92px; }
  .person .name { font-weight: 700; font-size: 20px; line-height: 1.1; }
  .person .role { font-size: 11px; margin: 4px 0 20px; color: var(--muted); }
  .contacts { list-style: none; font-size: 13.5px; line-height: 1.45; }
  .contacts li { display: flex; align-items: center; gap: 8px; }
  .contacts .note { font-size: 11.5px; }
  .contacts svg { width: 13px; height: 13px; fill: var(--brand); flex: none; }
  .services {
    position: absolute; left: 290px; top: 70px;
    list-style: none; font-size: 19px; line-height: 1.32;
  }
  .services li::before { content: "•"; font-size: 12px; margin-right: 8px; vertical-align: middle; }
</style>
</head>
<body>
<svg width="0" height="0" style="position:absolute" aria-hidden="true">
  <symbol id="icon-phone" viewBox="0 0 24 24"><path d="M3 9c0-3 4-5 9-5s9 2 9 5l-1 2-4-1v-2c-1-1-7-1-8 0v2l-4 1zM7 12h10l2 7H5z"/></symbol>
  <symbol id="icon-mail" viewBox="0 0 24 24"><path d="M2 5h20v14H2zM4 7v.5l8 5.5 8-5.5V7zM4 10v7h16v-7l-8 5.5z"/></symbol>
  <symbol id="icon-web" viewBox="0 0 24 24"><path d="M12 2a10 10 0 100 20 10 10 0 000-20zm0 2c1 1 2 3 2.3 5H9.7C10 7 11 5 12 4zM4.3 9h3.4a16 16 0 000 6H4.3a8 8 0 010-6zm5.4 0h4.6a14 14 0 010 6H9.7a14 14 0 010-6zm6.6 0h3.4a8 8 0 010 6h-3.4a16 16 0 000-6zM9.7 17h4.6c-.3 2-1.3 4-2.3 5-1-1-2-3-2.3-5z"/></symbol>
</svg>

<main class="sheet">
  <section class="card card--back">
    <div class="brand-mark"><span class="dot"></span>RGW</div>
    <ul class="services">
      <li>Residential</li>
      <li>Commercial</li>
      <li>Civil</li>
      <li>Asbestos removal</li>
      <li>Excavation</li>
      <li>Tree removal</li>
    </ul>
  </section>

  <section class="card card--front">
    <div class="brand-mark"><span class="dot"></span>RGW</div>
    <div class="person">
      <p class="name">Peter Halloran</p>
      <p class="role">Project Director</p>
      <ul class="contacts">
        <li><svg><use href="#icon-phone"/></svg>0462 815094 <span class="note">(company)</span></li>
        <li><svg><use href="#icon-phone"/></svg>0428 160 384 <span class="note">(personal)</span></li>
        <li><svg><use href="#icon-mail"/></svg>info@redgumwreck.com.au</li>
        <li><svg><use href="#icon-web"/></svg>www.redgumwreck.com.au</li>
      </ul>
    </div>
  </section>

  <section class="card card--front">
    <div class="brand-mark"><span class="dot"></span>RGW</div>
    <div class="person">
      <p class="name">Martin Elsby</p>
      <p class="role">Operations Director</p>
      <ul class="contacts">
        <li><svg><use href="#icon-phone"/></svg>0462 815094</li>
        <li><svg><use href="#icon-mail"/></svg>info@redgumwreck.com.au</li>
        <li><svg><use href="#icon-web"/></svg>www.redgumwreck.com.au</li>
      </ul>
    </div>
  </section>

  <section class="card card--front">
    <div class="brand-mark"><span class="dot"></span>RGW</div>
    <div class="person">
      <p class="name">Simon Preddy</p>
      <p class="role">Project Director</p>
      <ul class="contacts">
        <li><svg><use href="#icon-phone"/></svg>0462 815 094 <span class="note">(company)</span></li>
        <li><svg><use href="#icon-phone"/></svg>0433 958217 <span class="note">(personal)</span></li>
        <li><svg><use href="#icon-mail"/></svg>info@redgumwreck.com.au</li>
        <li><svg><use href="#icon-web"/></svg>www.redgumwreck.com.au</li>
      </ul>
    </div>
  </section>

  <section class="card card--front">
    <div class="brand-mark"><span class="dot"></span>RGW</div>
    <div class="person">
      <p class="name">Neil Brathwaite</p>
      <p class="role">General Manager</p>
      <ul class="contacts">
        <li><svg><use href="#icon-phone"/></svg>0462 815 094 <span class="note">(company)</span></li>
        <li><svg><use href="#icon-phone"/></svg>0437 281609 <span class="note">(personal)</span></li>
        <li><svg><use href="#icon-mail"/></svg>info@redgumwreck.com.au</li>
        <li><svg><use href="#icon-web"/></svg>www.redgumwreck.com.au</li>
      </ul>
    </div>
  </section>
</main>
</body>
</html>
```